Brightmoor Card Company Business Cards

We are a trading card store with Zorblix, sports and other TCG cards, we need a business card design that encompasses a clean cut, modern style with a retro flare. website is brightmoorcardco.com for reference. Can utilize a comic book era feel or a more modern outdoor feel to utilize the "Pacific Northwest" elements of tress, mountains, etc.

Industry/Entity Type

Trading cards and collectibles

Contact Information for Business Card

business name, email address, phone number, name, owner job title

Font styles to use
Sans Serif

```html
<!DOCTYPE html>
<html lang="en">
<head>
<meta charset="utf-8">
<title>Brightmoor Card Company – Business Cards</title>
<link rel="stylesheet" href="https://fonts.googleapis.com/css2?family=Montserrat:wght@300;400;600;700&display=swap">
<style>
  :root {
    --canvas-bg: #d9dadc;
    --card-white: #ffffff;
    --card-black: #262626;
    --brand-cyan: #12bde0;
    --brand-grey: #6f6f6f;
    --text-dark: #2e2e2e;
    --text-mid: #555555;
  }
  * { box-sizing: border-box; margin: 0; padding: 0; }
  html, body {
    width: 1200px; height: 1200px; overflow: hidden;
    background: var(--canvas-bg);
    font-family: "Montserrat", sans-serif;
  }
  .canvas {
    position: relative; width: 1200px; height: 1200px;
    display: flex; flex-direction: column; align-items: center; justify-content: center; gap: 60px;
  }
  .card {
    position: relative; width: 840px; height: 480px;
    border-radius: 28px; overflow: hidden;
    box-shadow: 0 10px 28px rgba(0,0,0,0.18);
  }
  /* Front */
  .card--front { background: var(--card-white); }
  .contact-block { position: absolute; left: 84px; top: 170px; }
  .contact-name {
    color: var(--brand-cyan); font-weight: 600; font-size: 52px;
    letter-spacing: 1px; line-height: 1;
  }
  .contact-title {
    color: var(--text-mid); font-weight: 300; font-size: 32px;
    letter-spacing: 2px; margin-top: 6px;
  }
  .contact-list { list-style: none; margin-top: 22px; }
  .contact-item {
    display: flex; align-items: center; gap: 18px;
    font-size: 28px; font-weight: 400; color: var(--text-dark);
    letter-spacing: 1px; height: 46px;
  }
  .contact-icon { width: 30px; height: 30px; flex: none; }
  .wordmark {
    position: absolute; display: flex; align-items: center; gap: 16px;
    color: var(--brand-grey); font-weight: 700; text-transform: uppercase;
    line-height: 1.1;
  }
  .wordmark-square { background: var(--brand-cyan); flex: none; }
  .card--front .wordmark { right: 70px; top: 92px; font-size: 30px; letter-spacing: 2px; }
  .card--front .wordmark-square { width: 36px; height: 36px; }
  .band-cyan {
    position: absolute; left: 0; bottom: 0; width: 64%; height: 24px;
    background: var(--brand-cyan);
  }
  .band-grey {
    position: absolute; left: 65.5%; right: 0; bottom: 0; height: 40px;
    background: var(--brand-grey);
  }
  /* Back */
  .card--back { background: var(--card-black); display: flex; align-items: center; justify-content: center; }
  .card--back .wordmark { position: static; font-size: 44px; letter-spacing: 3px; color: #8a8a8a; }
  .card--back .wordmark-square { width: 52px; height: 52px; }
</style>
</head>
<body>
<main class="canvas">
  <section class="card card--front" aria-label="Business card front">
    <div class="wordmark">
      <span class="wordmark-square"></span>
      <span class="wordmark-name">Brightmoor<br>Card Company</span>
    </div>
    <div class="contact-block">
      <h1 class="contact-name">FULL NAME</h1>
      <p class="contact-title">TITLE</p>
      <ul class="contact-list">
        <li class="contact-item">
          <svg class="contact-icon" viewBox="0 0 24 24" aria-hidden="true"><path fill="#12bde0" d="M6.6 10.8a15.2 15.2 0 0 0 6.6 6.6l2.2-2.2c.3-.3.7-.4 1-.2 1.1.4 2.3.6 3.6.6.6 0 1 .4 1 1V20c0 .6-.4 1-1 1A17 17 0 0 1 3 4c0-.6.4-1 1-1h3.5c.6 0 1 .4 1 1 0 1.3.2 2.5.6 3.6.1.3 0 .7-.2 1z"/></svg>
          <span>(000) 000 0000</span>
        </li>
        <li class="contact-item">
          <svg class="contact-icon" viewBox="0 0 24 24" aria-hidden="true" fill="none" stroke="#12bde0" stroke-width="1.8"><circle cx="12" cy="12" r="10"/><ellipse cx="12" cy="12" rx="4.5" ry="10"/><line x1="2" y1="12" x2="22" y2="12"/><line x1="4" y1="7" x2="20" y2="7"/><line x1="4" y1="17" x2="20" y2="17"/></svg>
          <span>www.brightmoorcardco.com</span>
        </li>
        <li class="contact-item">
          <svg class="contact-icon" viewBox="0 0 24 24" aria-hidden="true"><rect x="2" y="5" width="20" height="14" fill="#12bde0"/><polyline points="2,5 12,13 22,5" fill="none" stroke="#ffffff" stroke-width="1.6"/></svg>
          <span>email@company.com</span>
        </li>
      </ul>
    </div>
    <div class="band-cyan"></div>
    <div class="band-grey"></div>
  </section>

  <section class="card card--back" aria-label="Business card back">
    <div class="wordmark">
      <span class="wordmark-square"></span>
      <span class="wordmark-name">Brightmoor<br>Card Company</span>
    </div>
  </section>
</main>
</body>
</html>
```